Tatami Hall Sport promotional leaflet to attract new members

We are looking to produce a leaflet for a local judo club to attract seniors and juniors 5+ the leaflet needs to encourage people to attend classes and train in the martial art

Tatami Hall Sport are proud members of the KSB UK (mats for every) and practice traditional judo which mean we wear white Gi's to show cleanliness and tradition.

www.tatamihallsport.co.uk

Target Market(s)

Kids from 5+ and Adults

Font styles to use
Serif

Requirements
Must have
• Must include times of training and how to book onto a beginners induction
• it must look enticing and show that Judo is fun for all
• must highlight we open on Tuesdays and Thursdays
• Juniors are from 6.15pm to 7.15pm
• seniors 7.30pm to 9pm
• classes are held at Vantrel Gym, Unit 7, Marlow Row, Denholm Close, Rustington, West Sussex, BN17 8QT
• We practice on a Sprung floor Mat area and is great for men and women
• first two classes free
Nice to have
• Classes are run by an expeirnced team including
• Dan Merrow 5th Dan and international referee
• Luke Merrow 2nd Dan current Global Grappling Union European Champion

```html
<!DOCTYPE html>
<html lang="en">
<head>
<meta charset="utf-8">
<title>Tatami Hall Sport – Leaflet</title>
<link href="https://fonts.googleapis.com/css2?family=Abril+Fatface&family=Josefin+Sans:wght@300&display=swap" rel="stylesheet">
<style>
  :root {
    --navy: #1d2637;
    --red: #e31837;
    --white: #ffffff;
    --backdrop: #ececec;
    --display: "Abril Fatface", "Playfair Display", Georgia, serif;
    --brand: "Josefin Sans", Arial, sans-serif;
  }
  * { margin: 0; padding: 0; box-sizing: border-box; }
  html, body { width: 1200px; height: 1200px; overflow: hidden; }
  body { background: var(--backdrop); position: relative; font-family: var(--display); }

  .page {
    position: absolute;
    top: 250px;
    width: 496px;
    height: 700px;
    overflow: hidden;
  }
  .page--front { left: 89px; background: var(--white); }
  .page--back { left: 616px; background: var(--navy); }

  .front-art { position: absolute; inset: 0; width: 496px; height: 700px; }

  .brand {
    position: absolute;
    top: 26px; left: 0; right: 0;
    display: flex; justify-content: center; align-items: center; gap: 12px;
    color: var(--navy);
  }
  .brand__mark { width: 40px; height: 40px; border-radius: 50%; background: var(--red); }
  .brand__name {
    font-family: var(--brand);
    font-weight: 300;
    font-size: 35px;
    letter-spacing: 0.5px;
    text-transform: uppercase;
    line-height: 1;
    padding-top: 6px;
  }

  .session { position: absolute; top: 440px; color: var(--white); line-height: 1; }
  .session__name { font-size: 21px; letter-spacing: 0.3px; }
  .session__time { font-size: 12.5px; margin-top: 3px; }
  .session--juniors { left: 12px; }
  .session--seniors { right: 12px; text-align: left; }

  .open-on {
    position: absolute; top: 522px; left: 0; right: 0;
    text-align: center; color: var(--red);
    font-size: 50px; letter-spacing: 3px; line-height: 1;
    font-weight: 400;
  }
  .open-days {
    position: absolute; top: 573px; left: 0; right: 0;
    text-align: center; color: var(--white);
    font-size: 15px; letter-spacing: 0.6px; line-height: 1.2;
  }
  .mat-note {
    position: absolute; top: 615px; left: 0; right: 0;
    text-align: center; color: var(--white);
    font-size: 10px; letter-spacing: 0.2px; line-height: 1.2;
  }
  .offer {
    position: absolute; top: 651px; left: 0; right: 0;
    text-align: center; color: var(--red);
    font-size: 34px; letter-spacing: 1.6px; line-height: 1;
  }

  .team-photo {
    position: absolute; top: 0; left: 0;
    width: 496px; height: 332px;
    background: linear-gradient(180deg, #7c8088 0%, #9a9ea5 45%, #d9dcdf 75%, #c9cdd1 100%);
  }
  .team-heading {
    position: absolute; top: 354px; left: 0; right: 0;
    text-align: center; color: var(--red);
    font-size: 15px; letter-spacing: 1.2px; line-height: 1.2;
    font-weight: 400;
  }
  .team-line {
    position: absolute; left: 0; right: 0;
    text-align: center; color: var(--white);
    font-size: 11.5px; letter-spacing: 0.3px; line-height: 1.2;
  }
  .team-line--one { top: 378px; }
  .team-line--two { top: 398px; }

  .action-frame {
    position: absolute; top: 470px; left: 106px;
    width: 284px; height: 175px;
    background: linear-gradient(180deg, var(--navy) 0%, #7a1f32 60%, var(--red) 100%);
  }
  .action-photo {
    position: absolute; top: 440px; left: 118px;
    width: 260px; height: 192px;
    background: linear-gradient(180deg, #4b5058 0%, #6f747b 40%, #aeb3b5 70%, #9fa6a5 100%);
  }
  .venue {
    position: absolute; top: 659px; left: 0; right: 0;
    text-align: center; color: var(--red);
    font-size: 16px; line-height: 1;
  }
  .venue-address {
    position: absolute; top: 679px; left: 0; right: 0;
    text-align: center; color: var(--white);
    font-size: 11.5px; line-height: 1;
  }
</style>
</head>
<body>

  <section class="page page--front">
    <svg class="front-art" viewBox="0 0 413 584" preserveAspectRatio="none">
      <defs>
        <linearGradient id="greyBand" x1="0" y1="1" x2="1" y2="0">
          <stop offset="0" stop-color="#a9a9ae"/>
          <stop offset="1" stop-color="#ffffff"/>
        </linearGradient>
        <linearGradient id="redBand" x1="0" y1="0" x2="0" y2="1">
          <stop offset="0" stop-color="#1d2637"/>
          <stop offset="1" stop-color="#e31837"/>
        </linearGradient>
        <linearGradient id="photoTone" x1="0" y1="0" x2="0" y2="1">
          <stop offset="0" stop-color="#5d636b"/>
          <stop offset="0.5" stop-color="#c9c4bd"/>
          <stop offset="1" stop-color="#9fa6a8"/>
        </linearGradient>
      </defs>
      <polygon class="band band--grey" points="0,180 112,68 144,68 0,212" fill="url(#greyBand)"/>
      <polygon class="band band--grey" points="413,180 301,68 269,68 413,212" fill="url(#greyBand)"/>
      <polygon class="field" points="0,250 150,100 263,100 413,250 413,584 0,584" fill="#1d2637"/>
      <polygon class="band band--red" points="0,262 0,302 140,442 176,442" fill="url(#redBand)"/>
      <polygon class="band band--red" points="413,262 413,302 273,442 237,442" fill="url(#redBand)"/>
      <polygon class="frame frame--red" points="206,90 366,250 206,410 46,250" fill="#1d2637" stroke="#e31837" stroke-width="12"/>
      <polygon class="frame frame--white" points="206,122 334,250 206,378 78,250" fill="none" stroke="#ffffff" stroke-width="6"/>
      <g role="img" aria-label="Photo of a judo coach in a black belt with two junior students in white gi">
        <polygon points="206,132 324,250 206,368 88,250" fill="url(#photoTone)"/>
      </g>
    </svg>

    <header class="brand">
      <span class="brand__mark"></span>
      <span class="brand__name">Tatami Hall Sport</span>
    </header>

    <div class="session session--juniors">
      <div class="session__name">JUNIORS</div>
      <div class="session__time">6.15pm to 7.15pm</div>
    </div>
    <div class="session session--seniors">
      <div class="session__name">SENIORS</div>
      <div class="session__time">7.30pm to 9pm</div>
    </div>

    <h1 class="open-on">OPEN ON</h1>
    <p class="open-days">TUESDAYS AND THURSDAYS</p>
    <p class="mat-note">WE PRACTICE ON A SPRUNG FLOOR MAT AREA AND IS GREAT FOR MEN AND WOMEN</p>
    <p class="offer">FIRST TWO CLASSES FREE</p>
  </section>

  <section class="page page--back">
    <div class="team-photo" role="img" aria-label="Group photo of the club's judoka in white gi lined up on the mats in the training hall"></div>

    <h2 class="team-heading">CLASSES ARE RUN BY AN EXPEIRNCED TEAM INCLUDING</h2>
    <p class="team-line team-line--one">Dan Merrow 5th Dan and international referee</p>
    <p class="team-line team-line--two">Luke Merrow 2nd Dan current Global Grappling Union European Champion</p>

    <div class="action-frame"></div>
    <div class="action-photo" role="img" aria-label="Photo of judoka practising a throw on the sprung mat during a class"></div>

    <p class="venue">Classes are held at Vantrel Gym</p>
    <p class="venue-address">Unit 7, Marlow Row, Denholm Close, Rustington, West Sussex, BN17 8QT</p>
  </section>

</body>
</html>
```